Home page in PSD needed for a Business Consultant website

We have been given the mandate to re-do the website: http://www.velorancourt.ca/

Deliverable: home page in PSD format in French language

Context: Luc Brodeur is a business strategist specializing in marketing, creativity, business development. He helps small and medium companies develop their business through creative marketing strategies.

Some websites we like for your inspiration:

http://www.tallgreenbirch.com.au/
http://www.pdadvisory.com.au/
http://holtadvisors.com.au/
http://www.brumilotq.com/fr

Target Market(s)

B2B: Companies looking on the web for a business consultant who can help them with marketing, business developement, printing needs.

Industry/Entity Type

Business

Requirements
Must have
• Call to action: "Simplifiez votre développement des affaires" (which means "Simplify your business development")
• List of services (main menu)
• Marketing
• Développement des affaires
• Créativité
• Scolaire
• Impression
• Top menu as follow:
• Accueil
• À propos
• Contact

```html
<!DOCTYPE html>
<html lang="fr">
<head>
<meta charset="utf-8">
<title>Velorancourt Stratège — Luc Brodeur</title>
<link href="https://fonts.googleapis.com/css2?family=Arimo:ital,wght@0,400;0,700;1,400&family=Noto+Serif:wght@400;700&display=swap" rel="stylesheet">
<style>
:root{
  --blue:#0a74c4;
  --blue-dark:#075f9f;
  --charcoal:#2e2e2e;
  --nav-active:#5a5a5a;
  --ink:#1c1c1c;
  --body:#555;
  --line:#d8d8d8;
  --white:#fff;
  --sans:"Arimo", Arial, sans-serif;
  --serif:"Noto Serif", Georgia, serif;
}
*{box-sizing:border-box;margin:0;padding:0}
html,body{width:919px;height:1200px;overflow:hidden;background:var(--white)}
body{position:relative;font-family:var(--sans);color:var(--body)}

/* header */
.site-header{position:absolute;left:0;top:0;width:919px;height:79px;background:var(--blue)}
.header-shape{position:absolute;left:0;top:0}
.brand{position:absolute;left:112px;top:16px;width:240px;text-align:center}
.brand-name{font-family:var(--serif);font-size:21px;font-weight:400;color:#1a1a1a;white-space:nowrap}
.brand-tagline{font-size:7.5px;color:var(--blue-dark);letter-spacing:1.4px;margin-top:4px;white-space:nowrap}
.header-contact{position:absolute;left:672px;top:10px;display:flex;align-items:center}
.phone-badge{width:27px;height:28px;background:var(--white);border-radius:4px;display:flex;align-items:center;justify-content:center;margin-right:9px}
.header-contact .who{color:var(--white);font-weight:700;font-size:14.5px;line-height:15px}
.main-nav{position:absolute;left:428px;top:50px;height:29px;display:flex}
.main-nav a{display:block;height:29px;line-height:29px;color:var(--white);text-decoration:none;font-size:11px;padding:0 15px}
.main-nav a.active{background:var(--nav-active);padding:0 16px}

/* hero */
.hero{position:absolute;left:115px;top:107px;width:689px;height:249px;
  background:linear-gradient(135deg,#eef0f3 0%,#dfe3ea 45%,#c9d2df 75%,#aab5c6 100%)}
.hero-title{position:absolute;left:22px;top:159px;background:var(--blue);color:var(--white);font-size:20px;padding:0 10px;height:30px;line-height:30px;white-space:nowrap}
.hero-sub{position:absolute;left:80px;top:192px;background:#3b3b3b;color:var(--white);font-size:17px;height:28px;line-height:28px;padding:0 10px;white-space:nowrap}

/* about */
.about-photo{position:absolute;left:115px;top:384px;width:122px;height:141px;border:1px solid #cfcfcf;background:linear-gradient(180deg,#f3f3f3 0%,#e4e4e4 55%,#3a3c44 56%,#2c2e35 100%)}
.about{position:absolute;left:257px;top:383px;width:547px}
.about h2{font-family:var(--serif);font-weight:400;font-size:21px;color:var(--ink);margin-left:2px}
.about h2 span{color:var(--blue)}
.about p{font-size:9.6px;line-height:13px;text-align:justify;margin-top:14px}
.about p + p{margin-top:12px}

/* services band */
.services{position:absolute;left:0;top:560px;width:919px;height:279px;background:var(--blue)}
.services h2{font-family:var(--serif);font-weight:700;font-size:20px;color:var(--white);text-align:center;margin-top:11px}
.service-card{position:absolute;top:57px;width:201px;height:193px;background:var(--white)}
.service-card .thumb{position:absolute;left:8px;top:8px;width:184px;height:82px;border:1px solid #bbb}
.service-card h3{position:absolute;left:9px;top:97px;right:9px;font-family:var(--serif);font-size:12.5px;font-weight:400;color:var(--blue);line-height:13px}
.service-card h3 b{font-weight:700}
.service-card p{position:absolute;left:9px;right:11px;font-size:8.6px;line-height:11.3px;text-align:justify}
.read-more{position:absolute;right:0;bottom:0;width:90px;height:17px}
.read-more svg{position:absolute;left:0;top:0}
.read-more span{position:absolute;right:9px;top:3px;font-size:9px;color:var(--white);white-space:nowrap}

/* testimonials */
.testimonials h2{position:absolute;left:0;width:919px;top:859px;text-align:center;font-family:var(--serif);font-weight:700;font-size:21px;color:#333}
.quote-box{position:absolute;top:901px;width:316px;height:92px;border:1px solid var(--line);border-radius:3px;background:var(--white)}
.quote-box .mark{position:absolute;left:10px;top:8px;font-family:var(--serif);font-size:24px;color:#c2c2c2;line-height:24px}
.quote-box p{position:absolute;left:36px;right:15px;top:19px;font-style:italic;font-size:10.3px;line-height:13px;text-align:justify;color:#444}
.quote-box svg{position:absolute;left:32px;bottom:-10px}
.client{position:absolute;top:1006px}
.client .name{font-family:var(--serif);font-size:13px;color:var(--blue)}
.client .role{font-size:10px;color:var(--ink);margin-top:1px}

/* footer */
.site-footer{position:absolute;left:0;top:1073px;width:919px;height:127px;background:var(--charcoal)}
.footer-shape{position:absolute;left:0;top:0}
.foot-col{position:absolute;top:12px}
.foot-col h4{font-size:12px;font-weight:400;color:var(--white);margin-bottom:9px}
.foot-col ul{list-style:none}
.foot-col li{font-size:8.8px;color:#ddd;height:15.6px;white-space:nowrap}
.foot-item{display:flex;align-items:flex-start;font-size:8.6px;color:#ddd;line-height:10px;margin-bottom:9px}
.foot-item .ico{width:16px;flex:none}
.social{display:flex;align-items:center;margin-bottom:12px;font-size:8.6px;color:#ddd;line-height:10px}
.social .sq{width:16px;height:16px;background:#555;margin-right:8px;flex:none}
.social b{color:var(--white)}
.foot-brand{position:absolute;left:603px;top:38px;width:201px;text-align:center}
.foot-brand .brand-name{color:var(--white);font-size:20px}
.foot-brand .brand-tagline{color:#cfe4f5}
.copyright{position:absolute;right:115px;bottom:15px;font-size:8.6px;color:var(--white)}
</style>
</head>
<body>

<header class="site-header">
  <svg class="header-shape" width="919" height="79" viewBox="0 0 919 79">
    <polygon points="116,0 395,0 343,79 73,79" fill="#fff"/>
    <rect x="343" y="50" width="576" height="29" fill="#2e2e2e"/>
  </svg>
  <div class="brand">
    <div class="brand-name">Velorancourt Stratège</div>
    <div class="brand-tagline">commercialisation | marketing | créativité</div>
  </div>
  <div class="header-contact">
    <div class="phone-badge">
      <svg width="16" height="18" viewBox="0 0 16 18"><path d="M4 1 L7 5 L5 7 C6 10 8 12 10 13 L12 11 L15 14 L12 17 C6 16 1 10 1 4 Z" fill="#0a74c4"/></svg>
    </div>
    <div class="who">Luc Brodeur<br>514 555 0182</div>
  </div>
  <nav class="main-nav">
    <a class="active" href="#">Accueil</a>
    <a href="#">À propos</a>
    <a href="#">Services</a>
    <a href="#">Témoignages</a>
    <a href="#">Contact</a>
  </nav>
</header>

<section class="hero" role="img" aria-label="Photo de gens d'affaires examinant des graphiques autour d'un bureau">
  <div class="hero-title">STRATÈGE D'AFFAIRES</div>
  <div class="hero-sub">SIMPLIFIEZ VOTRE DÉVELOPPEMENT DES AFFAIRES</div>
</section>

<div class="about-photo" role="img" aria-label="Portrait de Luc Brodeur"></div>
<section class="about">
  <h2>À propos de <span>LUC BRODEUR</span></h2>
  <p>Lorem ipsum dolor sit amet, consectetur adipiscing elit. Sed placerat mauris at felis vehicula faucibus ac ac dui. Maecenas in mattis lectus. Donec gravida, purus ac lobortis condimentum, tellus justo euismod sapien, imperdiet eleifend nisl tellus sit amet lorem. Pellentesque vel suscipit arcu. Proin sollicitudin vel nunc non consequat. Maecenas dolor turpis, consequat eget adipiscing nec, sagittis sed est.</p>
  <p>Lorem ipsum dolor sit amet, consectetur adipiscing elit. Sed placerat mauris at felis vehicula faucibus ac ac dui. Maecenas in mattis lectus. Donec gravida, purus ac lobortis condimentum, tellus justo euismod sapien, imperdiet eleifend nisl tellus sit amet lorem.</p>
</section>

<section class="services">
  <h2>STRATÈGE D'AFFAIRES spécialisé en</h2>

  <article class="service-card" style="left:115px">
    <div class="thumb" role="img" aria-label="Schéma marketing esquissé avec un crayon" style="background:linear-gradient(135deg,#f4f1ea,#e2ddd2 60%,#d8c9a8)"></div>
    <h3>Stratégie <b>MARKETING</b></h3>
    <p style="top:118px">Lorem ipsum dolor sit amet, consectetur adipiscing elit. Curabitur et lectus vulputate, pharetra quam id, pharetra odio. Vestibulum eget enim vel quam.</p>
    <div class="read-more"><svg width="90" height="17"><polygon points="14,0 90,0 90,17 0,17" fill="#2e2e2e"/></svg><span>En savoir plus</span></div>
  </article>

  <article class="service-card" style="left:359px">
    <div class="thumb" role="img" aria-label="Homme d'affaires présentant des schémas de stratégie au tableau" style="background:linear-gradient(135deg,#4a4d52,#2b2d31 55%,#5b5f66)"></div>
    <h3><b>CRÉATIVITÉ</b> en affaires</h3>
    <p style="top:118px">Lorem ipsum dolor sit amet, consectetur adipiscing elit. Curabitur et lectus vulputate, pharetra quam id, pharetra odio. Vestibulum eget enim vel quam.</p>
    <div class="read-more"><svg width="90" height="17"><polygon points="14,0 90,0 90,17 0,17" fill="#2e2e2e"/></svg><span>En savoir plus</span></div>
  </article>

  <article class="service-card" style="left:603px">
    <div class="thumb" role="img" aria-label="Main utilisant une calculatrice sur des graphiques financiers" style="background:linear-gradient(135deg,#e9eef4,#cdd8e4 55%,#9fb2c8)"></div>
    <h3><b>DÉVELOPPEMENT</b><br>des affaires</h3>
    <p style="top:129px">Lorem ipsum dolor sit amet, consectetur adipiscing elit. Curabitur et lectus vulputate, pharetra quam id, pharetra odio.</p>
    <div class="read-more"><svg width="90" height="17"><polygon points="14,0 90,0 90,17 0,17" fill="#2e2e2e"/></svg><span>En savoir plus</span></div>
  </article>
</section>

<section class="testimonials">
  <h2>Témoignages clients</h2>

  <div class="quote-box" style="left:115px">
    <span class="mark">“</span>
    <p>Lorem ipsum dolor sit amet, consectetur adipiscing elit. Aliquam sed gravida aug ue. Nunc volutpat leo vel urna condimentum, eu pharetra lectus mollis. Nullam a arcu imperdiet, semper magna eget, imperdiet arcu .</p>
    <svg width="20" height="11"><polygon points="0,0 20,0 10,10" fill="#fff"/><polyline points="0,0 10,10 20,0" fill="none" stroke="#d8d8d8"/></svg>
  </div>
  <div class="client" style="left:138px"><div class="name">Dana Whitfield</div><div class="role">Lorem ipsum, dolor sit amet</div></div>

  <div class="quote-box" style="left:488px">
    <span class="mark">“</span>
    <p>Lorem ipsum dolor sit amet, consectetur adipiscing elit. Aliquam sed gravida aug ue. Nunc volutpat leo vel urna condimentum, eu pharetra lectus mollis. Nullam a arcu imperdiet, semper magna eget, imperdiet arcu .</p>
    <svg width="20" height="11"><polygon points="0,0 20,0 10,10" fill="#fff"/><polyline points="0,0 10,10 20,0" fill="none" stroke="#d8d8d8"/></svg>
  </div>
  <div class="client" style="left:514px"><div class="name">Dana Whitfield</div><div class="role">Lorem ipsum, dolor sit amet</div></div>
</section>

<footer class="site-footer">
  <svg class="footer-shape" width="919" height="127" viewBox="0 0 919 127">
    <polygon points="601,0 919,0 919,127 515,127" fill="#0a74c4"/>
    <line x1="598" y1="0" x2="512" y2="127" stroke="#fff" stroke-width="2"/>
  </svg>

  <div class="foot-col" style="left:116px">
    <h4>Nos services</h4>
    <ul><li>Marketing</li><li>Développement des affaires</li><li>Créativité</li><li>Scolaire</li><li>Impression</li></ul>
  </div>

  <div class="foot-col" style="left:250px">
    <h4>Contact</h4>
    <div class="foot-item"><span class="ico"><svg width="11" height="10" viewBox="0 0 11 10"><path d="M5.5 0 L11 5 L9 5 L9 10 L2 10 L2 5 L0 5 Z" fill="#aaa"/></svg></span><span>Lorem ipsum, dolor sit amet,<br>Consectetur lectus.</span></div>
    <div class="foot-item"><span class="ico"><svg width="10" height="11" viewBox="0 0 16 18"><path d="M4 1 L7 5 L5 7 C6 10 8 12 10 13 L12 11 L15 14 L12 17 C6 16 1 10 1 4 Z" fill="#aaa"/></svg></span><span>514 555 0182</span></div>
    <div class="foot-item"><span class="ico"></span><span>info@velorancourt.ca</span></div>
  </div>

  <div class="foot-col" style="left:438px">
    <h4>Suivez-moi</h4>
    <div class="social"><span class="sq"></span><span>Suivez-moi sur<br><b>Townsquare</b></span></div>
    <div class="social"><span class="sq"></span><span>Joignez-moi sur<br><b>Proflink</b></span></div>
  </div>

  <div class="foot-brand">
    <div class="brand-name">Velorancourt Stratège</div>
    <div class="brand-tagline">commercialisation | marketing | créativité</div>
  </div>
  <div class="copyright">© Velorancourt Stratège 2013. Tous droits réservés</div>
</footer>

</body>
</html>
```